Beacon Advisory Website

I currently have a website www.beaconadvisoryinc.example. We are a IT Consulting Company. Our website will pretty much tell out our services. I am looking to enhance my website and make it look more professional. Looking for very classy and Contemporary look and design for my website.

Industry/Entity Type

It Company

```html
<!DOCTYPE html>
<html lang="en">
<head>
<meta charset="utf-8">
<title>Beacon Advisory — IT Consulting</title>
<link href="https://fonts.googleapis.com/css2?family=Ubuntu:wght@300;400;500;700&family=Open+Sans:wght@400;600;700&display=swap" rel="stylesheet">
<style>
:root{
  --ink:#3d3d3d;
  --muted:#8a8a8a;
  --paper:#ffffff;
  --soft:#f4f4f4;
  --dark:#2a2a2a;
  --darker:#1b1b1b;
  --black:#0d0d0d;
  --blue:#1da1dd;
  --blue-deep:#1584bb;
  --pink:#d94b9c;
  --orange:#f2a23a;
  --teal:#1cc1c9;
  --green:#7dc242;
  --sky:#3aa8e6;
  --red:#e53935;
  --line:#d6d6d6;
}
*{box-sizing:border-box;margin:0;padding:0}
html,body{width:1200px;height:3884px;overflow:hidden}
body{font-family:"Open Sans",sans-serif;color:var(--ink);background:var(--paper);position:relative}
.abs{position:absolute}
h1,h2,h3{font-family:"Ubuntu",sans-serif;font-weight:400}

/* Hero */
.hero{position:absolute;left:0;top:0;width:1200px;height:520px;overflow:hidden}
.hero-photo{position:absolute;inset:0;background:linear-gradient(160deg,#4a4a4a 0%,#2e2e2e 45%,#1e1e1e 100%)}
.nav-bar{position:absolute;left:0;top:0;width:1200px;height:80px;background:rgba(0,0,0,.35)}
.brand{position:absolute;left:160px;top:22px;display:flex;align-items:center;gap:10px;font-family:"Ubuntu",sans-serif;font-weight:700;color:#fff;font-size:22px;letter-spacing:1px;text-transform:uppercase;white-space:nowrap}
.brand-mark{width:34px;height:34px;background:#fff}
.main-nav{position:absolute;left:512px;top:31px;display:flex;gap:15px;font-family:"Ubuntu",sans-serif;font-size:11px;color:#fff;letter-spacing:.5px;white-space:nowrap}
.nav-phone{position:absolute;left:940px;top:22px;height:32px;padding:0 14px;border:1px solid #fff;color:#fff;font-family:"Ubuntu",sans-serif;font-size:13px;line-height:30px;display:flex;gap:8px;align-items:center;white-space:nowrap}
.hero-title{position:absolute;left:0;width:1200px;top:160px;text-align:center;color:#fff;font-size:58px;line-height:70px;font-weight:400}
.hero-sub{position:absolute;left:0;width:1200px;top:362px;text-align:center;color:#fff;font-family:"Ubuntu",sans-serif;font-size:24px;display:flex;justify-content:center;align-items:center;gap:10px}

/* Section headings */
.sec-title{position:absolute;left:0;width:1200px;text-align:center;font-size:48px;letter-spacing:1px;color:#444}
.sec-sub{position:absolute;left:0;width:1200px;text-align:center;font-size:14px;color:var(--muted)}

/* Services */
.services{position:absolute;left:0;top:520px;width:1200px;height:760px;background:var(--paper)}
.service-label{position:absolute;font-family:"Ubuntu",sans-serif;font-size:11px;font-weight:500;letter-spacing:.5px;text-transform:uppercase;text-align:center;width:240px;white-space:nowrap}
.hub{position:absolute;left:405px;top:335px;width:390px;height:390px;border-radius:50%;background:var(--pink);border:10px solid #f6d6e8;color:#fff;text-align:center}
.hub h3{font-size:28px;margin-top:12px}
.hub p{font-size:13px;line-height:19px;width:260px;margin:12px auto 0}

/* Work */
.work{position:absolute;left:0;top:1280px;width:1200px;height:880px;background:var(--paper);border-top:1px solid #eee}
.showcase{position:absolute;left:120px;top:170px;width:680px;height:500px;background:linear-gradient(135deg,#f3d7e6 0%,#e9e9ee 40%,#cfd3da 75%,#b52a74 100%)}
.case-name{position:absolute;left:830px;top:310px;font-family:"Ubuntu",sans-serif;font-size:44px;font-weight:500;color:#2a2a2a}
.case-tag{position:absolute;left:832px;top:368px;font-size:11px;letter-spacing:1px;color:#555;text-transform:uppercase}
.case-text{position:absolute;left:832px;top:400px;width:230px;font-size:11px;line-height:16px;color:#555;text-transform:uppercase}
.platform-badge{position:absolute;left:720px;top:640px;width:70px;height:22px;border-radius:4px;background:#f08a2c}
.dots{position:absolute;left:0;width:1200px;top:692px;display:flex;justify-content:center;gap:8px}
.dots span{width:8px;height:8px;border-radius:50%;background:#ccc}
.dots span.on{background:#555}
.clients{position:absolute;left:120px;top:735px;width:960px;display:grid;grid-template-columns:repeat(7,1fr);row-gap:28px;column-gap:24px}
.clients span{height:24px;border-radius:12px;background:#cfcfcf}

/* Why us */
.why{position:absolute;left:0;top:2160px;width:1200px;height:820px;background:var(--dark)}
.why .sec-title{color:#fff}
.why .sec-sub{color:#6f6f6f}
.tabs{position:absolute;left:0;width:1200px;top:200px;display:flex;justify-content:center;gap:6px}
.tab{font-family:"Ubuntu",sans-serif;font-size:13px;color:#fff;padding:8px 20px;border:1px solid #555}
.tab.active{background:var(--black);border-color:var(--black)}
.step{position:absolute;top:285px;width:180px;text-align:center}
.step svg{display:block;margin:0 auto}
.step h4{font-family:"Ubuntu",sans-serif;font-weight:400;font-size:12px;color:#9a9a9a;letter-spacing:1px;margin-top:16px}
.step p{font-size:12px;line-height:17px;color:#fff;margin-top:26px;padding:0 14px;text-align:left}

/* Contact */
.contact{position:absolute;left:0;top:2980px;width:1200px;height:800px;background:var(--blue);overflow:hidden}
.contact h2{position:absolute;left:0;width:1200px;text-align:center;color:#fff;font-size:42px;line-height:52px;font-weight:500;top:22px}
.contact .lead{position:absolute;left:0;width:1200px;text-align:center;color:#fff;font-size:14px;top:160px}
.skyline{position:absolute;left:0;bottom:0;width:1200px;height:200px;background:linear-gradient(180deg,rgba(21,132,187,0) 0%,var(--blue-deep) 45%,#0f6e9e 100%)}
.callout{position:absolute;left:165px;top:205px;width:270px;height:270px;border-radius:50%;background:var(--black);color:#fff;text-align:center}
.callout .label{font-size:12px;margin-top:56px}
.callout .phone{font-family:"Ubuntu",sans-serif;font-size:26px;font-weight:500;margin-top:8px;white-space:nowrap}
.callout .note{font-size:9px;color:#bbb;margin:6px auto 0;width:180px;line-height:12px}
.callout .map{width:150px;height:60px;margin:10px auto 0;border-radius:4px;background:linear-gradient(90deg,#3a3a3a,#5a5a5a,#3a3a3a)}
.callout-notes{position:absolute;left:150px;top:495px;width:300px;text-align:center;color:#0b2c3d;font-size:10px;line-height:15px;text-transform:uppercase}
.form{position:absolute;left:520px;top:205px;width:520px;display:grid;grid-template-columns:1fr 1fr;column-gap:24px;row-gap:14px}
.field label{display:block;color:#fff;font-size:11px;margin-bottom:4px}
.field .box{height:30px;background:#fff}
.field .select{height:30px;background:#fff;font-size:11px;color:#777;padding:7px 10px}
.field.wide{grid-column:1 / 3}
.field .area{height:190px;background:#fff}
.submit{position:absolute;left:600px;top:628px;width:200px;text-align:center;font-family:"Ubuntu",sans-serif;font-size:13px;color:#0b2c3d;padding-bottom:6px;border-bottom:2px solid #0b2c3d;letter-spacing:1px}

/* Footer */
.footer{position:absolute;left:0;top:3780px;width:1200px;height:104px;background:var(--darker)}
.footer-nav{position:absolute;left:160px;top:40px;display:flex;gap:24px;font-family:"Ubuntu",sans-serif;font-size:12px;color:#fff;letter-spacing:.5px;white-space:nowrap}
.footer-brand{position:absolute;right:160px;top:22px;display:flex;align-items:center;gap:8px;font-family:"Ubuntu",sans-serif;font-weight:700;color:#fff;font-size:18px;text-transform:uppercase;letter-spacing:1px;white-space:nowrap}
.footer-brand .brand-mark{width:26px;height:26px}
.copyright{position:absolute;right:160px;top:64px;font-size:10px;color:#888;white-space:nowrap;text-align:right}
</style>
</head>
<body>

<header class="hero">
  <div class="hero-photo" role="img" aria-label="Dimmed photo of a workspace desk with laptop and coffee"></div>
  <div class="nav-bar"></div>
  <div class="brand"><span class="brand-mark"></span>Beacon Advisory</div>
  <nav class="main-nav"><span>COMPANY</span><span>PORTFOLIO</span><span>SERVICES</span><span>RESOURCES</span><span>CAREERS</span><span>CONTACT</span></nav>
  <div class="nav-phone">
    <svg width="12" height="12" viewBox="0 0 24 24"><path d="M6.6 10.8a15 15 0 006.6 6.6l2.2-2.2c.3-.3.7-.4 1-.2 1.1.4 2.3.6 3.6.6.6 0 1 .4 1 1V20c0 .6-.4 1-1 1C10.6 21 3 13.4 3 4c0-.6.4-1 1-1h3.5c.6 0 1 .4 1 1 0 1.3.2 2.5.6 3.6.1.3 0 .7-.2 1z" fill="#fff"/></svg>
    +1 (555) 010 4433
  </div>
  <h1 class="hero-title">We build successful digital<br>stories for web &amp; mobile</h1>
  <div class="hero-sub">Made With
    <svg width="26" height="24" viewBox="0 0 24 22"><path d="M12 21l-1.5-1.3C5 15 2 12.2 2 8.5 2 5.4 4.4 3 7.5 3c1.7 0 3.4.8 4.5 2.1C13.1 3.8 14.8 3 16.5 3 19.6 3 22 5.4 22 8.5c0 3.7-3 6.5-8.5 11.2z" fill="var(--red)"/></svg>
    and passion</div>
</header>

<section class="services">
  <h2 class="sec-title" style="top:28px">WE DESIGN, DEVELOP &amp; DELIVER</h2>
  <p class="sec-sub" style="top:90px">We Create exceptional web designs, ecommerce sites, mobile apps, digital campaigns &amp; much more.</p>

  <svg class="abs" style="left:0;top:0" width="1200" height="760" viewBox="0 0 1200 760">
    <path d="M264 608 A345 345 0 1 1 936 608" fill="none" stroke="var(--line)" stroke-width="2" stroke-dasharray="4 6"/>
    <g>
      <circle cx="600" cy="185" r="44" fill="var(--pink)" stroke="#f6d6e8" stroke-width="6"/>
      <g stroke="#fff" stroke-width="3" fill="#fff"><circle cx="600" cy="185" r="6"/><line x1="600" y1="185" x2="585" y2="170"/><line x1="600" y1="185" x2="616" y2="172"/><line x1="600" y1="185" x2="600" y2="204"/><circle cx="585" cy="170" r="4"/><circle cx="616" cy="172" r="4"/><circle cx="600" cy="204" r="4"/></g>
    </g>
    <g>
      <circle cx="378" cy="266" r="44" fill="var(--orange)" stroke="#fbe3c2" stroke-width="6"/>
      <path d="M362 266 l-10 0 M394 266 l10 0 M370 256 l-8 10 8 10 M386 256 l8 10 -8 10" stroke="#fff" stroke-width="3" fill="none" stroke-linecap="round"/>
    </g>
    <g>
      <circle cx="822" cy="266" r="44" fill="var(--teal)" stroke="#c6eff1" stroke-width="6"/>
      <rect x="802" y="250" width="40" height="28" fill="none" stroke="#fff" stroke-width="3"/>
      <path d="M808 272 l10-10 8 6 10-12" stroke="#fff" stroke-width="3" fill="none"/>
    </g>
    <g>
      <circle cx="264" cy="608" r="44" fill="var(--green)" stroke="#dcefc8" stroke-width="6"/>
      <rect x="244" y="592" width="40" height="26" rx="2" fill="none" stroke="#fff" stroke-width="3"/>
      <line x1="254" y1="626" x2="274" y2="626" stroke="#fff" stroke-width="3"/>
    </g>
    <g>
      <circle cx="936" cy="608" r="44" fill="var(--sky)" stroke="#cfe8f8" stroke-width="6"/>
      <path d="M918 618 h36 a10 10 0 0 0 -2 -20 a14 14 0 0 0 -26 -2 a10 10 0 0 0 -8 22z" fill="none" stroke="#fff" stroke-width="3"/>
    </g>
  </svg>
  <div class="service-label" style="left:480px;top:119px;color:var(--pink)">Enterprise Integration</div>
  <div class="service-label" style="left:258px;top:201px;color:var(--orange)">Web &amp; Software Development</div>
  <div class="service-label" style="left:702px;top:201px;color:var(--teal)">Business</div>
  <div class="service-label" style="left:144px;top:543px;color:var(--green)">Technology</div>
  <div class="service-label" style="left:816px;top:543px;color:var(--sky)">Cloud Services</div>

  <div class="hub">
    <svg width="90" height="80" viewBox="0 0 90 80" style="margin-top:40px">
      <g stroke="#fff" stroke-width="4" fill="#fff">
        <line x1="45" y1="40" x2="15" y2="15"/><line x1="45" y1="40" x2="75" y2="15"/><line x1="45" y1="40" x2="12" y2="62"/><line x1="45" y1="40" x2="78" y2="62"/><line x1="45" y1="40" x2="45" y2="75"/>
        <circle cx="45" cy="40" r="12"/><circle cx="15" cy="15" r="6"/><circle cx="75" cy="15" r="6"/><circle cx="12" cy="62" r="6"/><circle cx="78" cy="62" r="6"/><circle cx="45" cy="75" r="5"/>
      </g>
    </svg>
    <h3>Enterprise Integration</h3>
    <p>As organizations work to achieve and sustain competitive advantage, the ability for IT departments to deliver real value and measurable results to the business has increased dramatically.</p>
  </div>
</section>

<section class="work">
  <h2 class="sec-title" style="top:30px">HERE IS SOME OF OUR WORK</h2>
  <p class="sec-sub" style="top:100px">We work with leading brands and companies, providing cutting-edge technology, creative design, and business expertise.</p>
  <div class="showcase" role="img" aria-label="Online store project shown on desktop, laptop, tablet and phone screens with a pink paint splash"></div>
  <div class="case-name">formline</div>
  <div class="case-tag">Ready to shape your future</div>
  <div class="case-text">Responsive ecommerce store with fast checkout, custom catalogue, mobile layouts and tailored order tools.</div>
  <div class="platform-badge"></div>
  <div class="dots"><span class="on"></span><span></span><span></span><span></span></div>
  <div class="clients">
    <span></span><span></span><span></span><span></span><span></span><span></span><span></span>
    <span></span><span></span><span></span><span></span><span></span><span></span><span></span>
  </div>
</section>

<section class="why">
  <h2 class="sec-title" style="top:40px;color:#fff">WHY YOU SHOULD CHOOSE US?</h2>
  <p class="sec-sub" style="top:110px">We turn digital ideas into working products, with clear planning, careful design, solid build and steady support.</p>
  <div class="tabs"><span class="tab active">Our Process</span><span class="tab">About Us</span></div>

  <div class="step" style="left:130px">
    <svg width="110" height="110" viewBox="0 0 110 110"><circle cx="55" cy="55" r="48" fill="none" stroke="#3a3a3a" stroke-width="8"/><path d="M55 7 A48 48 0 0 1 103 55" fill="none" stroke="var(--blue)" stroke-width="8"/><circle cx="55" cy="55" r="34" fill="#202020"/><path d="M42 46 h22 v12 a10 10 0 0 1 -10 10 h-2 a10 10 0 0 1 -10 -10z M64 50 h4 a4 4 0 0 1 0 8 h-4" fill="none" stroke="#fff" stroke-width="3"/></svg>
    <h4>PLAN</h4>
    <p>Lorem ipsum dolor sit amet consectetur adipiscing elit Etiam feugiat urna leo sed</p>
  </div>
  <div class="step" style="left:318px">
    <svg width="110" height="110" viewBox="0 0 110 110"><circle cx="55" cy="55" r="48" fill="none" stroke="#3a3a3a" stroke-width="8"/><path d="M55 7 A48 48 0 1 1 7 55" fill="none" stroke="var(--blue)" stroke-width="8"/><circle cx="55" cy="55" r="34" fill="#202020"/><rect x="39" y="42" width="32" height="22" fill="none" stroke="#fff" stroke-width="3"/><line x1="48" y1="70" x2="62" y2="70" stroke="#fff" stroke-width="3"/></svg>
    <h4>DESIGN</h4>
    <p>Lorem ipsum dolor sit amet consectetur adipiscing elit Etiam feugiat urna leo sed</p>
  </div>
  <div class="step" style="left:510px">
    <svg width="110" height="110" viewBox="0 0 110 110"><circle cx="55" cy="55" r="48" fill="none" stroke="#3a3a3a" stroke-width="8"/><path d="M55 7 A48 48 0 0 1 55 103" fill="none" stroke="var(--blue)" stroke-width="8"/><circle cx="55" cy="55" r="34" fill="#202020"/><path d="M44 45 l-9 10 9 10 M66 45 l9 10 -9 10 M59 42 l-8 26" fill="none" stroke="#fff" stroke-width="3"/></svg>
    <h4>BUILD</h4>
    <p>Lorem ipsum dolor sit amet consectetur adipiscing elit Etiam feugiat urna leo sed</p>
  </div>
  <div class="step" style="left:694px">
    <svg width="110" height="110" viewBox="0 0 110 110"><circle cx="55" cy="55" r="48" fill="none" stroke="#3a3a3a" stroke-width="8"/><path d="M55 7 A48 48 0 1 1 14 30" fill="none" stroke="var(--blue)" stroke-width="8"/><circle cx="55" cy="55" r="34" fill="#202020"/><path d="M55 38 c8 8 8 20 4 28 h-8 c-4 -8 -4 -20 4 -28z M51 66 l-6 6 M59 66 l6 6" fill="none" stroke="#fff" stroke-width="3"/></svg>
    <h4>LAUNCH</h4>
    <p>Lorem ipsum dolor sit amet consectetur adipiscing elit Etiam feugiat urna leo sed</p>
  </div>
  <div class="step" style="left:870px">
    <svg width="110" height="110" viewBox="0 0 110 110"><circle cx="55" cy="55" r="48" fill="none" stroke="#3a3a3a" stroke-width="8"/><path d="M55 7 A48 48 0 0 1 96 79" fill="none" stroke="var(--blue)" stroke-width="8"/><circle cx="55" cy="55" r="34" fill="#202020"/><path d="M40 70 V40 M40 70 H72 M46 62 l8-10 6 5 10-13" fill="none" stroke="#fff" stroke-width="3"/></svg>
    <h4>MARKET</h4>
    <p>Lorem ipsum dolor sit amet consectetur adipiscing elit Etiam feugiat urna leo sed</p>
  </div>
</section>

<section class="contact">
  <h2>LETS TALK BUSINESS<br>TELL US ABOUT YOUR PROJECT AND BUDGET</h2>
  <p class="lead">Please take a quick moment to complete this form and a business representative will get back to you soon.</p>
  <div class="skyline" role="img" aria-label="Silhouette of a city skyline along the bottom edge"></div>

  <div class="callout">
    <div class="label">Contact Us</div>
    <div class="phone">+1 (555) 010 4433</div>
    <div class="note">Get expert help and lower cost support from our team</div>
    <div class="map" role="img" aria-label="World map"></div>
  </div>
  <div class="callout-notes">Reach us for professional IT consulting and support<br>Serving clients across the country<br>Call or write to our team today</div>

  <div class="form">
    <div class="field"><label>* First Name</label><div class="box"></div></div>
    <div class="field"><label>* Last Name</label><div class="box"></div></div>
    <div class="field"><label>* Email</label><div class="box"></div></div>
    <div class="field"><label>* Phone</label><div class="box"></div></div>
    <div class="field"><label>Company</label><div class="box"></div></div>
    <div class="field"><label>* State</label><div class="select">Select State</div></div>
    <div class="field wide"><label>Your Message</label><div class="area"></div></div>
  </div>
  <div class="submit">SUBMIT</div>
</section>

<footer class="footer">
  <nav class="footer-nav"><span>COMPANY</span><span>PORTFOLIO</span><span>SERVICES</span><span>RESOURCES</span><span>CAREERS</span><span>CONTACT</span></nav>
  <div class="footer-brand"><span class="brand-mark"></span>Beacon Advisory</div>
  <div class="copyright">Copyright © 2014 Beacon Advisory</div>
</footer>

</body>
</html>
```